Rack Card for Harbor Lens Studios

Looking to make a verticle rack card back and front 3.5 X 8.5, add .125 on each side for bleed, CMYK, need .psd file and all fonts. We are based out of Connecticut but we are adding a location in Florida so it needs to be beach themed. I have a sample photo image but something else could be used. Front side should have image, logo, back side should have pricing. For your reference our Connecticut site is www.hlsbridalfilms.com but the Florida site will be
www.hlsgc.com
941-555-0127

Target Market(s)

Brides

Industry/Entity Type

Wedding Photography

Requirements
Must have
• Beach theme

```html
<!DOCTYPE html>
<html lang="en">
<head>
<meta charset="utf-8">
<title>Harbor Lens Studios Rack Card</title>
<link rel="stylesheet" href="https://fonts.googleapis.com/css2?family=Cinzel:wght@400;600&family=Oswald:wght@300;500;600&display=swap">
<style>
  :root {
    --stage: #e9e9e9;
    --paper: #ffffff;
    --ink-dark: #1d1d1f;
    --ink-grey: #555555;
    --navy: #15173b;
    --red: #e8273a;
    --orange: #f39a1e;
    --green: #17693a;
    --ribbon: #c3e4f4;
    --bar: #000000;
  }
  html, body { margin: 0; padding: 0; overflow: hidden; }
  .stage {
    position: relative;
    width: 1200px;
    height: 1189px;
    background: var(--stage);
    overflow: hidden;
  }
  .card { position: absolute; display: block; box-shadow: 0 4px 14px rgba(0,0,0,.25); }
  .card-front { left: 81px; top: 55px; }
  .card-back { left: 618px; top: 113px; }
  .brand-front { font-family: "Cinzel", serif; font-weight: 600; fill: var(--ink-dark); }
  .tagline { font-family: "Cinzel", serif; font-weight: 600; fill: var(--ink-grey); }
  .brand-back { font-family: "Oswald", sans-serif; font-weight: 500; fill: var(--navy); }
  .pkg-title { font-family: "Oswald", sans-serif; font-weight: 600; fill: #fff; }
  .pkg-line { font-family: "Oswald", sans-serif; font-weight: 300; fill: #fff; }
  .pkg-price { font-family: "Oswald", sans-serif; font-weight: 600; fill: #fff; }
  .include-title { font-family: "Oswald", sans-serif; font-weight: 600; fill: var(--ink-dark); }
  .include-line { font-family: "Oswald", sans-serif; font-weight: 300; fill: var(--ink-dark); }
  .contact { font-family: "Oswald", sans-serif; font-weight: 600; fill: #fff; }
</style>
</head>
<body>
<div class="stage">

  <!-- Front -->
  <svg class="card card-front" width="441" height="1027" viewBox="0 0 548 1276" xmlns="http://www.w3.org/2000/svg">
    <defs>
      <linearGradient id="sunset" x1="0" y1="0" x2="0" y2="1">
        <stop offset="0" stop-color="#d8b4a6"/>
        <stop offset="0.22" stop-color="#efc48e"/>
        <stop offset="0.31" stop-color="#f6b43a"/>
        <stop offset="0.36" stop-color="#c99a6a"/>
        <stop offset="0.5" stop-color="#8f7a78"/>
        <stop offset="0.65" stop-color="#9a7a6c"/>
        <stop offset="1" stop-color="#5e4650"/>
      </linearGradient>
    </defs>
    <rect class="card-paper" width="548" height="1276" fill="var(--paper)"/>
    <path class="photo" role="img" aria-label="Bride and groom embracing on the beach at sunset"
          d="M0 0 H548 V960 Q274 1060 0 990 Z" fill="url(#sunset)"/>
    <text class="brand-front" x="274" y="92" font-size="50" text-anchor="middle">HARBOR LENS</text>
    <text class="brand-front" x="274" y="150" font-size="46" text-anchor="middle">STUDIOS</text>
    <text class="tagline" x="274" y="1072" font-size="47" text-anchor="middle">Unobtrusive</text>
    <text class="tagline" x="274" y="1129" font-size="47" text-anchor="middle">Documentary</text>
    <text class="tagline" x="274" y="1186" font-size="47" text-anchor="middle">Cinematic</text>
    <text class="tagline" x="274" y="1243" font-size="47" text-anchor="middle">videography</text>
  </svg>

  <!-- Back -->
  <svg class="card card-back" width="441" height="1027" viewBox="0 0 548 1276" xmlns="http://www.w3.org/2000/svg">
    <rect class="card-body" width="548" height="1276" fill="var(--navy)"/>
    <path class="header-panel" d="M0 0 H548 V140 Q274 270 0 140 Z" fill="var(--paper)"/>
    <path class="award-ribbon" d="M402 0 H520 V235 L461 215 L402 235 Z" fill="var(--ribbon)"/>
    <text class="brand-back" x="205" y="95" font-size="50" text-anchor="middle">HARBOR LENS</text>
    <text class="brand-back" x="205" y="145" font-size="40" text-anchor="middle">STUDIOS</text>

    <!-- Ceremony only -->
    <circle cx="129" cy="385" r="117" fill="var(--paper)"/>
    <circle cx="129" cy="385" r="105" fill="var(--navy)"/>
    <text class="pkg-title" x="129" y="350" font-size="24" text-anchor="middle" textLength="150" lengthAdjust="spacingAndGlyphs">CEREMONY ONLY</text>
    <text class="pkg-line" x="129" y="374" font-size="16" text-anchor="middle">UP TO 1 HOUR OF</text>
    <text class="pkg-line" x="129" y="393" font-size="16" text-anchor="middle">COVERAGE.</text>
    <text class="pkg-price" x="129" y="436" font-size="38" text-anchor="middle">$399</text>

    <!-- Deluxe -->
    <circle cx="382" cy="450" r="172" fill="var(--paper)"/>
    <circle cx="382" cy="450" r="158" fill="var(--red)"/>
    <text class="pkg-title" x="382" y="366" font-size="28" text-anchor="middle" textLength="196" lengthAdjust="spacingAndGlyphs">DELUXE PACKAGE</text>
    <text class="pkg-line" x="382" y="393" font-size="17" text-anchor="middle">UP TO 6 HOURS OF COVERAGE.</text>
    <text class="pkg-line" x="382" y="419" font-size="17" text-anchor="middle">BACKGROUND MUSIC WHERE SUITABLE.</text>
    <text class="pkg-line" x="382" y="445" font-size="17" text-anchor="middle">NAMES OF THE BRIDAL PARTY AND FAMILY.</text>
    <text class="pkg-line" x="382" y="471" font-size="17" text-anchor="middle">HIGHLIGHTS EDITED TO YOUR SONG CHOICE.</text>
    <text class="pkg-line" x="382" y="497" font-size="17" text-anchor="middle">AN ONLINE RECAP OF THE WEDDING</text>
    <text class="pkg-line" x="382" y="523" font-size="17" text-anchor="middle">TWO EXTRA DVD COPIES</text>
    <text class="pkg-line" x="382" y="541" font-size="17" text-anchor="middle">IN CUSTOM CASES.</text>
    <text class="pkg-price" x="382" y="584" font-size="38" text-anchor="middle">$1299</text>

    <!-- Classic -->
    <circle cx="129" cy="665" r="142" fill="var(--paper)"/>
    <circle cx="129" cy="665" r="129" fill="var(--orange)"/>
    <text class="pkg-title" x="129" y="626" font-size="26" text-anchor="middle" textLength="184" lengthAdjust="spacingAndGlyphs">CLASSIC PACKAGE</text>
    <text class="pkg-line" x="129" y="653" font-size="17" text-anchor="middle">UP TO 5 HOURS OF COVERAGE.</text>
    <text class="pkg-line" x="129" y="680" font-size="17" text-anchor="middle">BACKGROUND MUSIC WHERE SUITABLE.</text>
    <text class="pkg-line" x="129" y="707" font-size="17" text-anchor="middle">NAMES OF THE BRIDAL</text>
    <text class="pkg-line" x="129" y="726" font-size="17" text-anchor="middle">PARTY AND FAMILY.</text>
    <text class="pkg-price" x="129" y="772" font-size="38" text-anchor="middle">$999</text>

    <!-- Extras -->
    <circle cx="394" cy="840" r="190" fill="var(--paper)"/>
    <circle cx="394" cy="840" r="176" fill="var(--green)"/>
    <text class="pkg-title" x="394" y="752" font-size="40" text-anchor="middle">EXTRAS</text>
    <text class="pkg-line" x="394" y="790" font-size="21" text-anchor="middle">HOURLY COVERAGE $100/HOUR</text>
    <text class="pkg-line" x="394" y="826" font-size="21" text-anchor="middle">ENTIRE WEDDING ON THE CLOUD $100</text>
    <text class="pkg-line" x="394" y="863" font-size="21" text-anchor="middle">DRONE AERIAL COVERAGE $250/HOUR</text>
    <text class="pkg-line" x="394" y="900" font-size="21" text-anchor="middle">MONTAGE UP TO 25 PHOTOS $150</text>
    <text class="pkg-line" x="394" y="937" font-size="21" text-anchor="middle">BLU RAY COPY $50</text>
    <text class="pkg-line" x="394" y="972" font-size="21" text-anchor="middle">DVD COPY $25</text>

    <!-- Included -->
    <path class="footer-panel" d="M0 1228 V1115 Q274 1020 548 1115 V1228 Z" fill="var(--paper)"/>
    <text class="include-title" x="274" y="1116" font-size="30" text-anchor="middle">ALL PACKAGES INCLUDE:</text>
    <text class="include-line" x="182" y="1160" font-size="20" text-anchor="middle">BROADCAST QUALITY EQUIPMENT SHOT IN HD</text>
    <text class="include-line" x="182" y="1192" font-size="20" text-anchor="middle">REMOTE MICROPHONE FOR CLEAR AUDIO</text>
    <text class="include-line" x="444" y="1160" font-size="20" text-anchor="middle">PROFESSIONAL EDITING</text>
    <text class="include-line" x="444" y="1192" font-size="20" text-anchor="middle">PERSONALIZED DVD</text>

    <!-- Contact bar -->
    <rect class="contact-bar" x="0" y="1228" width="548" height="48" fill="var(--bar)"/>
    <path class="phone-icon" fill="#fff"
          d="M22 1243 c2-2 4-2 5 0 l3 5 c1 2 0 3-1 4 l-2 1 c1 3 4 6 7 7 l1-2 c1-1 2-2 4-1 l5 3 c2 1 2 3 0 5 l-2 2 c-3 3-10 0-15-5 s-8-12-5-15 Z"/>
    <text class="contact" x="48" y="1264" font-size="28">941-555-0127</text>
    <text class="contact" x="536" y="1264" font-size="28" text-anchor="end">WWW.HLSGC.COM</text>
  </svg>

</div>
</body>
</html>
```